Popup Banners - BrightCounsel - Legal Technology

- We need two banners (same style) designed with two different images and different text.

- The details of the printing requirements are attached, along with suggested images.

- The banners should share the same theme as our website www.brightcounsel.com.au

- The first banner would include our logo (attached), use the 'roads join' image (attached) in some way and text: New Opportunities - Where legal services and technology meet.

- The second banner would include our logo (attached), use the 'jigsaw' image (attached) in some way and use text: Legal Technology Strategy, Advice and Capability.

- Details on what are required from the Printer is attached also.

Target Market(s)

Legal Professionals

Industry/Entity Type

Information Technology

Font styles to use
Sans Serif

Requirements
Must have
• Our logo (attached), suggested text and the image mentioned for each.
Nice to have
• Professional and modern look
Should not have
• Cheap looking

```html
<!DOCTYPE html>
<html lang="en">
<head>
<meta charset="utf-8">
<title>BrightCounsel – Legal Technology Banner</title>
<link rel="stylesheet" href="https://fonts.googleapis.com/css2?family=Oswald:wght@300;400&family=Questrial&display=swap">
<style>
  :root {
    --stage: #141618;
    --header-white: #ffffff;
    --brand-grey: #4a4746;
    --brand-blue: #4a9fd8;
    --navy-deep: #0a2743;
    --navy-mid: #123c63;
    --photo-glow: #cfe6f7;
    --photo-light: #7fb3da;
    --band: rgba(170, 180, 192, 0.55);
    --text-light: #ffffff;
  }
  * { margin: 0; padding: 0; box-sizing: border-box; }
  html, body {
    width: 1200px;
    height: 1200px;
    overflow: hidden;
    background: var(--stage);
  }
  .canvas {
    position: relative;
    width: 1200px;
    height: 1200px;
  }
  .banner {
    position: absolute;
    left: 377px;
    top: 50px;
    width: 446px;
    height: 1100px;
    overflow: hidden;
    background: var(--navy-deep);
  }
  .banner-header {
    position: absolute;
    inset: 0 0 auto 0;
    height: 134px;
    background: var(--header-white);
    display: flex;
    align-items: center;
    justify-content: center;
    gap: 18px;
  }
  .brand-square {
    width: 26px;
    height: 26px;
    background: var(--brand-blue);
  }
  .brand-name {
    font-family: "Questrial", sans-serif;
    font-size: 31px;
    letter-spacing: 0.2em;
    color: var(--brand-grey);
  }
  .hero-photo {
    position: absolute;
    left: 0;
    right: 0;
    top: 134px;
    bottom: 0;
    background:
      radial-gradient(ellipse 55% 22% at 62% 18%, var(--photo-glow) 0%, rgba(207,230,247,0) 100%),
      radial-gradient(ellipse 60% 28% at 55% 48%, rgba(127,179,218,0.85) 0%, rgba(127,179,218,0) 100%),
      linear-gradient(180deg, var(--navy-mid) 0%, #1d5582 35%, #2b6a99 55%, var(--navy-mid) 78%, var(--navy-deep) 100%);
  }
  .headline-band {
    position: absolute;
    left: 0;
    right: 0;
    top: 363px;
    height: 204px;
    background: var(--band);
    display: flex;
    align-items: center;
    justify-content: center;
  }
  .headline {
    font-family: "Oswald", sans-serif;
    font-weight: 300;
    font-size: 50px;
    line-height: 57px;
    letter-spacing: 0.04em;
    color: var(--text-light);
    text-align: center;
    text-transform: uppercase;
  }
  .web-address {
    position: absolute;
    left: 0;
    right: 0;
    top: 950px;
    font-family: "Oswald", sans-serif;
    font-weight: 300;
    font-size: 46px;
    letter-spacing: 0.03em;
    color: var(--text-light);
    text-align: center;
  }
</style>
</head>
<body>
  <main class="canvas">
    <section class="banner">
      <header class="banner-header">
        <span class="brand-square"></span>
        <span class="brand-name">BrightCounsel</span>
      </header>
      <div class="hero-photo" role="img" aria-label="Close-up photo of fingers fitting together backlit jigsaw puzzle pieces in blue light"></div>
      <div class="headline-band">
        <h1 class="headline">Legal Technology<br>Strategy, Advice<br>and Capability</h1>
      </div>
      <p class="web-address">brightcounsel.com.au</p>
    </section>
  </main>
</body>
</html>
```